Metal Fabrication Business Official Opening Party Invitation

We need a postcard designed to promote the official opening celebration of our business.

Dimensions can be:
148mm x 105mm OR 210 x 148mm
Flat card please - not folded - CAN be double sided if that suits your design better

We are a metal fabrication business which designs, engineers, repairs and manufactures a range of custom, quality metal works including vehicle trays, agricultural machinery implements, trailers, wood splitters, fire pits, furniture etc.
The brand position focuses on custom work of the highest quality.
The design for this piece should be INDUSTRIAL, (prefer a darker perhaps metal background) whilst still being fun and semi rustic. It's a party after all - but a party about metal. It will be winter so it's OK to have a "cold" feel - one of our products are firepits.

If you have questions or would like more specific information please ask.

Branding guidelines are attached. Feel free to go outside of these guidelines to add more creativity and fun to this particular design

Also attached some invited we found online that we like some parts of - VERY open to ideas and creativity, just as a bit of an idea what we like :) We'd LOVE something original and creative.
Updates

Target Market(s)

Males aged 30 - 60yrs
Country area - farmers and tradespeople

Industry/Entity Type

Business

Requirements
Must have
• Must be a unique, industrial (steel/metal) theme.
• Can include things like cogs/gears, screws etc in the design.
• see the attached 'invite likes..." also
• Text to be included in design include:
• Harrow Ironworks (can just use logo) official opening
• Date: Fri Aug 26
• Location: 5678 Road title
• Time: 6:00pm
• "Join us to celebrate the official opening of Harrow Ironworks"
• Light dinner provided
Should not have
• NO SHINY METAL FINISHES PLEASE

```html
<!DOCTYPE html>
<html lang="en">
<head>
<meta charset="utf-8">
<title>Harrow Ironworks – Official Opening Invitation</title>
<link rel="stylesheet" href="https://fonts.googleapis.com/css2?family=Cinzel:wght@400;700;900&display=swap">
<style>
  :root {
    --page: #ffffff;
    --plate-light: #b9babb;
    --plate-dark: #7d7f81;
    --bar-dark: #2f3032;
    --bar-mid: #57595b;
    --steel-light: #e4e5e6;
    --steel-mid: #a9abad;
    --steel-deep: #6c6e70;
    --ink: #1b1c1e;
    --name-grey: #5c5e60;
    --brand-green: #5fbd3f;
    --brand-navy: #16244a;
    --soft-white: #eef1f6;
    --rivet: #8d8f91;
  }
  html, body {
    margin: 0;
    padding: 0;
    width: 838px;
    height: 1200px;
    overflow: hidden;
    background: var(--page);
  }
  .sheet {
    position: relative;
    width: 838px;
    height: 1200px;
  }
  .card {
    position: absolute;
    left: 22px;
    width: 794px;
    height: 564px;
    display: block;
  }
  .card--front { top: 26px; }
  .card--back { top: 621px; }
  .arc-text {
    font-family: "Cinzel", serif;
    font-weight: 700;
    font-size: 19px;
    fill: var(--ink);
  }
  .arc-text--navy { fill: var(--brand-navy); font-size: 24px; font-weight: 900; }
  .brand-name {
    font-family: "Cinzel", serif;
    font-weight: 900;
    fill: var(--name-grey);
    text-anchor: middle;
  }
  .brand-name--light { fill: var(--steel-light); }
  .event-date {
    font-family: "Cinzel", serif;
    font-weight: 900;
    font-size: 58px;
    fill: var(--brand-navy);
    text-anchor: middle;
  }
  .event-address {
    font-family: "Cinzel", serif;
    font-weight: 400;
    font-size: 24px;
    fill: var(--soft-white);
    text-anchor: middle;
  }
  .event-time {
    font-family: "Cinzel", serif;
    font-weight: 900;
    font-size: 31px;
    fill: var(--brand-navy);
    text-anchor: middle;
  }
  .dinner-line {
    font-family: "Cinzel", serif;
    font-weight: 400;
    font-size: 27px;
    fill: var(--soft-white);
    text-anchor: middle;
  }
  .dinner-strong {
    font-family: "Cinzel", serif;
    font-weight: 900;
    font-size: 37px;
    fill: var(--soft-white);
    text-anchor: middle;
  }
  .rivet { fill: var(--rivet); stroke: var(--bar-dark); stroke-width: 1.5; }
</style>
</head>
<body>
<main class="sheet">

  <!-- Front of card -->
  <svg class="card card--front" viewBox="0 0 926 658" xmlns="http://www.w3.org/2000/svg">
    <defs>
      <linearGradient id="plateTone" x1="0" y1="0" x2="1" y2="1">
        <stop offset="0" stop-color="var(--plate-light)"/>
        <stop offset="1" stop-color="var(--plate-dark)"/>
      </linearGradient>
      <linearGradient id="barTone" x1="0" y1="0" x2="0" y2="1">
        <stop offset="0" stop-color="var(--bar-mid)"/>
        <stop offset="1" stop-color="var(--bar-dark)"/>
      </linearGradient>
      <linearGradient id="bandTone" x1="0" y1="0" x2="1" y2="0">
        <stop offset="0" stop-color="var(--steel-mid)"/>
        <stop offset="0.5" stop-color="var(--steel-light)"/>
        <stop offset="1" stop-color="var(--steel-mid)"/>
      </linearGradient>
      <linearGradient id="ringTone" x1="0" y1="0" x2="1" y2="1">
        <stop offset="0" stop-color="#f2f3f4"/>
        <stop offset="1" stop-color="var(--steel-mid)"/>
      </linearGradient>
      <radialGradient id="gearTone" cx="0.5" cy="0.5" r="0.5">
        <stop offset="0.7" stop-color="var(--steel-light)"/>
        <stop offset="1" stop-color="var(--steel-deep)"/>
      </radialGradient>
      <radialGradient id="hubTone" cx="0.5" cy="0.5" r="0.5">
        <stop offset="0.6" stop-color="#ffffff"/>
        <stop offset="1" stop-color="#d6d8da"/>
      </radialGradient>
      <path id="frontTopArc" d="M 170 325 A 294 294 0 0 1 758 325"/>
      <path id="frontBottomArc" d="M 154 325 A 310 310 0 0 0 774 325"/>
    </defs>

    <rect class="tread-plate" width="926" height="658" fill="url(#plateTone)" role="img" aria-label="Diamond tread steel plate texture"/>

    <rect class="steel-band" y="220" width="926" height="208" fill="url(#bandTone)"/>
    <rect class="rail" y="178" width="926" height="42" fill="url(#barTone)"/>
    <rect class="rail" y="428" width="926" height="42" fill="url(#barTone)"/>
    <g class="rail-rivets">
      <circle class="rivet" cx="42" cy="199" r="6"/><circle class="rivet" cx="126" cy="199" r="6"/>
      <circle class="rivet" cx="210" cy="199" r="6"/><circle class="rivet" cx="716" cy="199" r="6"/>
      <circle class="rivet" cx="800" cy="199" r="6"/><circle class="rivet" cx="884" cy="199" r="6"/>
      <circle class="rivet" cx="42" cy="449" r="6"/><circle class="rivet" cx="126" cy="449" r="6"/>
      <circle class="rivet" cx="210" cy="449" r="6"/><circle class="rivet" cx="716" cy="449" r="6"/>
      <circle class="rivet" cx="800" cy="449" r="6"/><circle class="rivet" cx="884" cy="449" r="6"/>
    </g>

    <rect class="hardware" x="4" y="226" width="170" height="170" rx="30" fill="var(--steel-deep)" opacity="0.55" role="img" aria-label="Large hex nut"/>
    <rect class="hardware" x="774" y="250" width="150" height="160" rx="20" fill="var(--steel-deep)" opacity="0.45" role="img" aria-label="Crossed bolts with nuts"/>

    <circle class="medallion-ring" cx="464" cy="325" r="325" fill="url(#ringTone)"/>
    <circle class="medallion-face" cx="464" cy="325" r="268" fill="var(--bar-dark)"/>
    <circle class="gear" cx="464" cy="325" r="212" fill="url(#gearTone)" role="img" aria-label="Steel cog with bolted teeth"/>
    <circle class="gear-hub" cx="464" cy="325" r="162" fill="url(#hubTone)"/>

    <text class="arc-text" letter-spacing="2"><textPath href="#frontTopArc" startOffset="50%" text-anchor="middle">JOIN US TO CELEBRATE THE OFFICIAL OPENING OF</textPath></text>
    <text class="arc-text" letter-spacing="2"><textPath href="#frontBottomArc" startOffset="50%" text-anchor="middle">JOIN US TO CELEBRATE THE OFFICIAL OPENING OF</textPath></text>

    <g class="brand-lockup">
      <text class="brand-name" x="464" y="318" font-size="52">HARROW</text>
      <text class="brand-name" x="464" y="364" font-size="30" letter-spacing="4">IRONWORKS</text>
    </g>
  </svg>

  <!-- Back of card -->
  <svg class="card card--back" viewBox="0 0 926 658" xmlns="http://www.w3.org/2000/svg">
    <defs>
      <linearGradient id="plateToneBack" x1="0" y1="0" x2="1" y2="1">
        <stop offset="0" stop-color="var(--plate-light)"/>
        <stop offset="1" stop-color="var(--plate-dark)"/>
      </linearGradient>
      <linearGradient id="barToneBack" x1="0" y1="0" x2="0" y2="1">
        <stop offset="0" stop-color="var(--bar-mid)"/>
        <stop offset="1" stop-color="var(--bar-dark)"/>
      </linearGradient>
      <linearGradient id="ringToneBack" x1="0" y1="0" x2="1" y2="1">
        <stop offset="0" stop-color="#f2f3f4"/>
        <stop offset="1" stop-color="var(--steel-mid)"/>
      </linearGradient>
      <radialGradient id="greenTone" cx="0.5" cy="0.5" r="0.6">
        <stop offset="0" stop-color="#6ccb49"/>
        <stop offset="1" stop-color="var(--brand-green)"/>
      </radialGradient>
      <clipPath id="innerDisc"><circle cx="464" cy="331" r="272"/></clipPath>
      <path id="backTopArc" d="M 170 331 A 294 294 0 0 1 758 331"/>
      <path id="backBottomArc" d="M 160 331 A 304 304 0 0 0 768 331"/>
    </defs>

    <rect class="tread-plate" width="926" height="658" fill="url(#plateToneBack)" role="img" aria-label="Diamond tread steel plate texture"/>

    <rect class="skyline" x="6" y="40" width="200" height="110" fill="var(--steel-deep)" opacity="0.3" role="img" aria-label="Embossed factory skyline"/>
    <rect class="skyline" x="720" y="40" width="200" height="110" fill="var(--steel-deep)" opacity="0.3" role="img" aria-label="Embossed factory skyline"/>

    <circle class="medallion-ring" cx="464" cy="331" r="320" fill="url(#ringToneBack)"/>
    <g clip-path="url(#innerDisc)">
      <rect class="panel-top" x="150" y="40" width="630" height="170" fill="var(--brand-navy)"/>
      <rect class="panel-mid" x="150" y="210" width="630" height="240" fill="url(#greenTone)"/>
      <rect class="panel-low" x="150" y="450" width="630" height="170" fill="var(--brand-navy)"/>
    </g>

    <rect class="rail" y="191" width="926" height="45" fill="url(#barToneBack)"/>
    <rect class="rail" y="426" width="926" height="48" fill="url(#barToneBack)"/>
    <g class="rail-rivets">
      <circle class="rivet" cx="42" cy="213" r="6"/><circle class="rivet" cx="126" cy="213" r="6"/>
      <circle class="rivet" cx="210" cy="213" r="6"/><circle class="rivet" cx="294" cy="213" r="6"/>
      <circle class="rivet" cx="378" cy="213" r="6"/><circle class="rivet" cx="462" cy="213" r="6"/>
      <circle class="rivet" cx="546" cy="213" r="6"/><circle class="rivet" cx="630" cy="213" r="6"/>
      <circle class="rivet" cx="714" cy="213" r="6"/><circle class="rivet" cx="798" cy="213" r="6"/>
      <circle class="rivet" cx="882" cy="213" r="6"/>
      <circle class="rivet" cx="42" cy="450" r="6"/><circle class="rivet" cx="126" cy="450" r="6"/>
      <circle class="rivet" cx="210" cy="450" r="6"/><circle class="rivet" cx="294" cy="450" r="6"/>
      <circle class="rivet" cx="378" cy="450" r="6"/><circle class="rivet" cx="462" cy="450" r="6"/>
      <circle class="rivet" cx="546" cy="450" r="6"/><circle class="rivet" cx="630" cy="450" r="6"/>
      <circle class="rivet" cx="714" cy="450" r="6"/><circle class="rivet" cx="798" cy="450" r="6"/>
      <circle class="rivet" cx="882" cy="450" r="6"/>
    </g>

    <rect class="hardware" x="30" y="488" width="200" height="160" rx="20" fill="var(--steel-deep)" opacity="0.45" role="img" aria-label="Crossed bolts with nuts"/>
    <rect class="hardware" x="730" y="484" width="190" height="170" rx="30" fill="var(--steel-deep)" opacity="0.55" role="img" aria-label="Large hex nut with bolt"/>

    <text class="arc-text" letter-spacing="2"><textPath href="#backTopArc" startOffset="50%" text-anchor="middle">JOIN US TO CELEBRATE THE OFFICIAL OPENING OF</textPath></text>

    <g class="brand-lockup">
      <text class="brand-name brand-name--light" x="464" y="154" font-size="38" letter-spacing="1">HARROW</text>
      <text class="brand-name brand-name--light" x="464" y="180" font-size="18" letter-spacing="5">IRONWORKS</text>
    </g>

    <text class="event-date" x="464" y="321">FRI AUG 26</text>
    <text class="event-address" x="464" y="353">5678 ROAD TITLE</text>
    <text class="event-time" x="464" y="394">TIME: 6:00PM</text>

    <text class="dinner-line" x="464" y="513">LIGHT DINNER</text>
    <text class="dinner-strong" x="464" y="561">PROVIDED</text>

    <text class="arc-text arc-text--navy" letter-spacing="2"><textPath href="#backBottomArc" startOffset="50%" text-anchor="middle">YOU ARE INVITED</textPath></text>
  </svg>

</main>
</body>
</html>
```